Granite Tile Retail Website

We need wireframe PSD for a website selling granite tile. There are 4 custom pages, shopping cart page, and checkout page. I have a logo designed but the color scheme is up to you.
Please look at design-explanation.docx as I got through each page with more detail.
Home - I mocked up the home page so you know the layout (lg-home.jpg). This is where I need you to spend the most time to make a very appealing design.
Color Gallery - We have approximately 20 different stone colors. Each color will have a little gallery of its own pictures. On this page the customer can also add a sample piece of the color they are viewing to their shopping cart.
Questions Page - This page has 3 elements
1. Upload or fax diagram of kitchen for quotation
2. Installation video
3. Installation FAQ (text)
Order Page - This page has 3 steps for the customer
1. Customer chooses his color.
2. For each color we have numerous different products. He inputs the quantity of each product.
3. Customer is given total price and shipping quote. If order over $500 it says "This order qualifies for free shipping". Customer can click on button to "Order Now"
Shopping Cart - Very standard, just like I have attached here. Just modify for your colors / font.
Checkout - Just like in the attached. See design-explanation.docx for minor adjustments.
I have vector file for logo.
Updates
Please try to post your designs by tonightÂ
Target Market(s)
Home owners 40-60 years old
Industry/Entity Type
Shopping
Look and feel

```html
<!DOCTYPE html>
<html lang="en">
<head>
<meta charset="utf-8">
<title>Brisk Stone – Home</title>
<link rel="stylesheet" href="https://fonts.googleapis.com/css2?family=Arimo:wght@400;700&family=EB+Garamond:ital,wght@1,500;1,700&display=swap">
<style>
:root{
  --accent-top:#f2b45a;
  --page-bg:#4f2527;
  --header-bg:#5b2b2d;
  --panel:#ffffff;
  --orange:#ee9a1c;
  --orange-light:#f7b43c;
  --orange-dark:#d9800c;
  --maroon:#7b2f31;
  --maroon-dark:#5a1d1f;
  --video:#4a4a4a;
  --ink:#3c2a22;
  --body-text:#555555;
  --footer-text:#e8d8d2;
  --copyright:#d9923a;
  --white:#ffffff;
}
*{margin:0;padding:0;box-sizing:border-box}
html,body{width:1200px;height:1200px;overflow:hidden}
body{background:var(--page-bg);font-family:"Arimo",Arial,sans-serif;position:relative}
.top-rule{position:absolute;left:0;top:0;width:1200px;height:7px;background:var(--accent-top)}
.site{position:absolute;left:54px;top:7px;width:1092px;height:1164px;background:var(--header-bg)}
.brand{position:absolute;left:26px;top:58px;display:flex;align-items:center;gap:12px;color:var(--white);font-weight:700}
.brand-mark{width:22px;height:22px;background:var(--orange)}
.brand-name{font-size:38px;letter-spacing:7px;line-height:1}
.brand-sub{display:block;font-size:15px;letter-spacing:8px;margin-top:6px;padding-left:22px}
.main-nav{position:absolute;top:95px;right:20px;display:flex;align-items:center;gap:0}
.main-nav a{color:var(--white);text-decoration:none;font-size:17px;padding:9px 19px;border-radius:3px}
.main-nav a.active{background:linear-gradient(var(--orange-light),var(--orange-dark))}
.content{position:absolute;left:1px;top:172px;width:1091px;height:817px;background:var(--panel)}
.hero{position:absolute;left:11px;top:9px;width:1069px;height:415px;background:linear-gradient(160deg,var(--orange-light),var(--orange) 55%,var(--orange-dark))}
.video-frame{position:absolute;left:32px;top:57px;width:558px;height:313px;background:#fff;padding:6px;box-shadow:0 14px 16px -8px rgba(120,60,0,.45)}
.video-frame div{width:100%;height:100%;background:var(--video)}
.hero-copy{position:absolute;left:626px;top:62px;width:420px;font-family:"EB Garamond",Georgia,serif;font-style:italic}
.hero-title{color:var(--white);font-size:29px;font-weight:700;letter-spacing:.5px}
.hero-text{color:var(--ink);font-size:24px;font-weight:500;line-height:33px;margin-top:8px}
.btn-more{position:absolute;left:649px;top:304px;width:326px;height:46px;border-radius:5px;background:linear-gradient(var(--maroon),var(--maroon-dark));color:var(--white);font-size:21px;display:flex;align-items:center;padding-left:75px;box-shadow:0 8px 10px -4px rgba(90,40,0,.5)}
.btn-more svg{position:absolute;right:22px;top:11px}
.features{position:absolute;left:11px;top:433px;width:1069px;height:148px;display:flex;gap:4px}
.feature{position:relative;flex:1}
.feature-photo{position:absolute;inset:0}
.feature.q .feature-photo{background:linear-gradient(135deg,#1f5a8e,#6fa3cf 60%,#d8e6f1)}
.feature.c .feature-photo{background:linear-gradient(90deg,#b8885a,#b56e78 30%,#7d4b45 55%,#c99ca0 75%,#9fa3a8)}
.feature.g .feature-photo{background:linear-gradient(90deg,#5a6b7d,#a89a88 45%,#8d97a6)}
.feature-label{position:absolute;left:16px;top:87px;width:324px;height:40px;background:linear-gradient(#fff,#e9e9e9);border-radius:2px;display:flex;align-items:center;padding-left:22px;color:var(--maroon-dark);font-size:26px}
.feature-label span{position:absolute;right:0;top:0;width:48px;height:40px;background:linear-gradient(var(--orange-light),var(--orange-dark));display:flex;align-items:center;justify-content:center}
.intro{position:absolute;left:13px;top:608px;width:845px;font-size:12.6px;line-height:26px;color:var(--body-text)}
.samples{position:absolute;left:869px;top:604px;width:211px;height:147px;background:linear-gradient(135deg,#c6a37a,#a5707e 45%,#c8b9c2 75%,#9fa6ad)}
.site-footer{position:absolute;left:0;top:1019px;width:1092px}
.footer-links{position:absolute;top:0;list-style:none}
.footer-links li{font-size:13.5px;color:var(--footer-text);line-height:26px}
.footer-links.col1{left:39px}
.footer-links.col2{left:214px}
.footer-brand{position:absolute;left:921px;top:12px;display:flex;align-items:center;gap:8px;color:var(--white);font-weight:700}
.footer-brand .brand-mark{width:12px;height:12px}
.footer-brand .brand-name{font-size:20px;letter-spacing:4px}
.footer-brand .brand-sub{font-size:8px;letter-spacing:4px;margin-top:3px;padding-left:12px}
.social{position:absolute;left:920px;top:82px;display:flex;gap:7px}
.social span{width:20px;height:20px;border-radius:3px}
.copyright{position:absolute;left:0;top:1186px;width:1200px;text-align:center;font-size:12.5px;color:var(--copyright)}
</style>
</head>
<body>
<div class="top-rule"></div>
<div class="site">
  <header>
    <div class="brand">
      <span class="brand-mark"></span>
      <div><span class="brand-name">BRISK</span><span class="brand-sub">STONE</span></div>
    </div>
    <nav class="main-nav">
      <a class="active" href="#">HOME</a>
      <a href="#">GALLERY</a>
      <a href="#">QUESTIONS</a>
      <a href="#">ORDER</a>
      <a href="#">SHIPPING CART</a>
    </nav>
  </header>

  <main class="content">
    <section class="hero">
      <div class="video-frame"><div role="img" aria-label="Installation video player"></div></div>
      <div class="hero-copy">
        <h1 class="hero-title">LOREM IPSUM DOLOR SIT</h1>
        <p class="hero-text">Lorem ipsum dolor sit amet, consectetuer adipiscing elit. Aenean commodo ligula eget dolor. Aenean massa. Cum sociis natoque penatibus et magnis dis parturient montes, nascetur ridiculus mus.</p>
      </div>
      <a class="btn-more">LEARN MORE
        <svg width="34" height="24" viewBox="0 0 34 24"><path d="M3 3l9 9-9 9M16 3l9 9-9 9" fill="none" stroke="#fff" stroke-width="4"/></svg>
      </a>
    </section>

    <section class="features">
      <div class="feature q">
        <div class="feature-photo" role="img" aria-label="Blue granite stair steps"></div>
        <div class="feature-label">Questions?<span><svg width="24" height="18" viewBox="0 0 24 18"><path d="M2 2l7 7-7 7M12 2l7 7-7 7" fill="none" stroke="#fff" stroke-width="3"/></svg></span></div>
      </div>
      <div class="feature c">
        <div class="feature-photo" role="img" aria-label="Strips of granite colour samples"></div>
        <div class="feature-label">Color Selection<span><svg width="24" height="18" viewBox="0 0 24 18"><path d="M2 2l7 7-7 7M12 2l7 7-7 7" fill="none" stroke="#fff" stroke-width="3"/></svg></span></div>
      </div>
      <div class="feature g">
        <div class="feature-photo" role="img" aria-label="Smiling customer beside granite samples"></div>
        <div class="feature-label">Get A Quote<span><svg width="24" height="18" viewBox="0 0 24 18"><path d="M2 2l7 7-7 7M12 2l7 7-7 7" fill="none" stroke="#fff" stroke-width="3"/></svg></span></div>
      </div>
    </section>

    <p class="intro">Lorem ipsum dolor sit amet, consectetuer adipiscing elit. Aenean commodo ligula eget dolor. Aenean massa. Cum sociis natoque penati-bus et magnis dis parturient montes, nascetur ridiculus mus. Donec quam felis, ultricies nec, pellentesque eu, pretium quis, sem. Nulla consequat massa quis eniLorem ipsum dolor sit amet, consectetuer adipiscing elit. Aenean commodo ligula eget dolor. Aenean massa. Cum sociis natoque penatibus et magnis dis parturient montes, nascetur ridiculus mus. Donec quam felis, ultricies nec, pellentesque eu, pretium quis, sem. Nulla consequat massa quis eniLorem ipsum dolor sit amet, consectetuer adipiscing elit. Aenean commodo ligula eget dolor. Aenean massa. Cum sociis natoque penatibus et magnis dis parturient montes, nascetur ridiculus mus. Donec quam felis, ultricies nec, pellentesque eu, pretium quis, sem. Nulla consequat massa quis eni</p>
    <div class="samples" role="img" aria-label="Fanned stack of granite tile samples"></div>
  </main>

  <footer class="site-footer">
    <ul class="footer-links col1">
      <li>Home</li><li>Gallery</li><li>Questions</li><li>Order</li><li>Shipping Cart</li>
    </ul>
    <ul class="footer-links col2">
      <li>Return Policy</li><li>Shipping Policy</li><li>Privacy</li><li>Terms of Use</li><li>Customer Service</li>
    </ul>
    <div class="footer-brand">
      <span class="brand-mark"></span>
      <div><span class="brand-name">BRISK</span><span class="brand-sub">STONE</span></div>
    </div>
    <div class="social" aria-label="Social links">
      <span style="background:#3b5b99"></span>
      <span style="background:#4aa3d8"></span>
      <span style="background:#c8302a"></span>
      <span style="background:#2a6ea8"></span>
      <span style="background:#e57a1f"></span>
    </div>
  </footer>
</div>
<p class="copyright">Copyright © 2011 briskstone.com</p>
</body>
</html>
```